single page with calendar booking ability

a single web page that has the ability to book calendar times and dates, also needs to be able to link to my other business social media seamlessly. I don't want to get multiple developers and or agency's involved, I want you the web designer to design it and make sure it's up and works as described
. The boats we work on are between 20 feet to 40 feet, bow riders , cabin cruisers, and center consoles. The brands that we work on include but are not limited to Veltora, Pirelle, Kelo marsh, Tidwick, Castavel, Brenlo, Quill, and many more. Winterization and shrink wrapping is completely different than graphic wrapping, we do not do graphic's wrapping. Also, only 5% of our business will be auto detailing, the rest will be boats on trailers. Please ensure that the calendar booking system is intergraded and not a surprise to me later

Target Market(s)

Lakes region New Hampshire

Industry/Entity Type

marine

Coding

Coded - Design and coding required

Number of Pages Required

1 page

Colors
0054AA
0677BA
7BADD7
CADEEF
E8F1F8
00AB8E
00BBA5
67D7C9
C6EFE9
E9F9F6
EE7325
F08F49
F5BC92
FAE3D3
FDF4ED

Requirements
Must have
• calendar booking capability
Nice to have
• Pictures of boats being shrink wrapped for the winter season, Nice before and after pictures of boats detailed, only 5% of our business is auto detailing
Should not have
• Large yachts, lots of sail boats as we only do a few, graphics wrapping.. we don't graphic wrap

```html
<!DOCTYPE html>
<html lang="en">
<head>
<meta charset="utf-8">
<title>Harbor Crest Marine &amp; Auto</title>
<link href="https://fonts.googleapis.com/css2?family=Montserrat:wght@400;500;600;700;800&display=swap" rel="stylesheet">
<style>
:root{
  --blue-dark:#0054AA;
  --blue:#0677BA;
  --blue-mid:#7BADD7;
  --blue-light:#CADEEF;
  --blue-pale:#E8F1F8;
  --teal:#00AB8E;
  --teal-pale:#C6EFE9;
  --orange:#EE7325;
  --orange-red:#F04E23;
  --orange-soft:#F08F49;
  --orange-pale:#FAE3D3;
  --ink:#222428;
  --text:#555a60;
  --line:#c9ccd1;
  --white:#fff;
}
*{margin:0;padding:0;box-sizing:border-box}
html,body{width:1200px;height:4666px;overflow:hidden;background:var(--white)}
body{font-family:'Montserrat',sans-serif;color:var(--ink)}
.page{position:relative;width:1200px;height:4666px;overflow:hidden}
.abs{position:absolute}
.btn{position:absolute;display:flex;align-items:center;justify-content:center;background:var(--orange);color:var(--white);border-radius:40px;font-weight:500;text-decoration:none}
.accent{color:var(--blue)}

/* hero */
.hero{left:0;top:0;width:1200px;height:760px;background:linear-gradient(180deg,#6f6a86 0%,#c98a6c 22%,#8c6f78 32%,#2f4f86 45%,#1d3f7d 70%,#2b5c9a 100%)}
.hero-wave{left:0;top:0}
.logo-name{font-weight:800;font-size:26px;letter-spacing:.5px;line-height:1.05;color:var(--white);text-transform:uppercase}
.logo-mark{width:22px;height:22px;border-radius:50%;background:var(--orange);display:inline-block}
.nav{top:64px;font-size:15px;font-weight:600;color:var(--white);text-transform:uppercase}
.nav.current{color:var(--orange)}
.hero-title{left:112px;top:200px;font-size:56px;font-weight:700;line-height:64px;color:var(--white);text-transform:uppercase}
.checks{left:112px;top:358px;list-style:none}
.checks li{display:flex;align-items:center;gap:10px;font-size:20px;font-weight:600;color:var(--white);height:36px}
.dots{left:573px;top:542px;display:flex;gap:4px}
.dots span{width:13px;height:13px;border-radius:50%;border:2px solid var(--white)}
.dots span.on{background:var(--white)}

/* welcome */
.welcome-title{left:112px;top:752px;width:400px;font-size:38px;font-weight:700;line-height:48px;text-transform:uppercase}
.welcome-lead{left:530px;top:755px;width:570px;font-size:17.5px;font-weight:600;line-height:29px}
.welcome-body{left:530px;top:860px;width:560px;font-size:15px;line-height:27px;color:var(--text)}

/* section titles */
.section-title{left:0;width:1200px;text-align:center;font-size:38px;font-weight:700;text-transform:uppercase}

/* services */
.services{left:0;top:1008px;width:1200px;height:706px;background:var(--blue-pale)}
.card{top:1155px;width:310px;height:485px;background:var(--white);text-align:center}
.card.raised{box-shadow:0 6px 18px rgba(0,40,90,.18)}
.card-photo{width:310px;height:242px}
.card h3{margin-top:24px;font-size:22px;font-weight:500;line-height:28px;padding:0 20px}
.card p{margin-top:18px;font-size:15px;line-height:27px;color:var(--text);padding:0 10px}
.card .more{display:block;margin-top:14px;font-size:15px;font-weight:600;color:var(--orange);text-decoration:none}

/* pricing */
.price-circle{border-radius:50%}
.price-block{text-align:center;color:var(--text);font-size:16px;line-height:27px}
.price-block h4{font-size:29px;font-weight:600;color:var(--ink);margin-bottom:12px}
.price-block p{margin-bottom:26px}
.price-block b{font-size:21px;font-weight:600;color:var(--ink)}
.price-hot{color:var(--white);text-align:center;font-size:15px;line-height:20px}
.price-hot h4{font-size:21px;font-weight:600;line-height:27px;margin-bottom:22px}
.price-hot b{font-size:21px;font-weight:600}
.price-hot p{margin-bottom:29px}

/* different */
.diff-photo{left:0;top:2380px;width:600px;height:686px;background:linear-gradient(180deg,#e4e9ef 0%,#cfd9e6 15%,#2e56c7 38%,#1a3ba6 60%,#3b3d44 80%,#8d8b86 100%)}
.diff-panel{left:600px;top:2380px;width:600px;height:686px;background:linear-gradient(160deg,var(--blue) 0%,var(--blue-dark) 100%)}
.diff-title{left:665px;top:2440px;font-size:39px;font-weight:700;line-height:49px;color:var(--white);text-transform:uppercase}
.diff-item{left:653px;display:flex;align-items:center;gap:28px;color:var(--white);font-size:21px;font-weight:600;line-height:28px}
.diff-icon{width:80px;height:80px;border-radius:50%;background:var(--white);display:flex;align-items:center;justify-content:center;flex:none}

/* calendar */
.calendar{left:112px;top:3227px;width:478px;height:395px;border:1px solid var(--line);border-radius:10px;overflow:hidden;background:var(--white)}
.cal-head{height:50px;display:flex;align-items:center;justify-content:space-between;padding:0 28px;font-size:20px;font-weight:500}
.cal-grid{display:grid;grid-template-columns:repeat(7,1fr)}
.cal-grid .dow{height:30px;background:var(--blue);color:var(--white);font-size:13px;font-weight:600;display:flex;align-items:center;justify-content:center;border-right:1px solid #2a8fcb}
.cal-grid .day{height:63px;border-right:1px solid #e1e4e8;border-bottom:1px solid #e1e4e8;font-size:12px;text-align:right;padding:8px 8px 0 0}
.day.booked{background:var(--teal-pale)}
.day.hold{background:var(--orange-pale)}
.legend{left:170px;top:3650px;display:flex;gap:28px;font-size:14px;font-weight:500}
.legend span{display:flex;align-items:center;gap:10px}
.legend i{width:22px;height:22px;border:1px solid var(--line);display:inline-block}
.form-label{left:624px;width:464px;text-align:center;font-size:19px;font-weight:500}
.field{position:absolute;height:43px;border:1px solid #b9bdc2;background:var(--white);font-size:15px;color:#6a6e74;padding:0 12px;display:flex;align-items:center;justify-content:space-between}
.toggle{position:absolute;top:3427px;height:36px;display:flex;align-items:center;justify-content:center;font-size:15px;font-weight:500}

/* ready */
.ready{left:0;top:3743px;width:1200px;height:601px;background:linear-gradient(95deg,#0a6fb8 0%,#1c84c6 35%,#6fb2e0 60%,#cfe4f4 85%,#eaf3fa 100%)}
.ready-title{left:112px;top:3822px;font-size:39px;font-weight:700;line-height:52px;color:var(--white);text-transform:uppercase}
.ready-text{left:112px;top:3953px;width:420px;font-size:15px;line-height:30px;color:var(--white)}

/* footer */
.foot-name{left:112px;top:4430px;font-size:34px;font-weight:800;line-height:40px;color:var(--blue-dark);text-transform:uppercase}
.foot-head{top:4348px;font-size:19px;font-weight:500}
.foot-links{left:514px;top:4388px;list-style:none;font-size:16px;line-height:30px;color:var(--text)}
.foot-contact{left:711px;font-size:19px;font-weight:500;display:flex;align-items:center;gap:10px}
.foot-rule{left:112px;top:4582px;width:976px;height:1px;background:#e2e4e7}
.copyright{left:112px;top:4603px;font-size:15px;color:var(--text)}
.social{top:4593px;width:40px;height:40px;border-radius:50%;border:1.5px solid var(--orange)}
</style>
</head>
<body>
<div class="page">

  <!-- hero -->
  <div class="abs hero" role="img" aria-label="Photo of a speedboat cruising across the lake at sunset"></div>
  <svg class="abs hero-wave" width="1200" height="760" viewBox="0 0 1200 760" aria-hidden="true">
    <path d="M0 618 C 180 700 400 700 640 632 C 860 572 1060 560 1200 760 L0 760 Z" fill="#fff"/>
  </svg>

  <div class="abs" style="left:112px;top:52px;display:flex;align-items:center;gap:10px">
    <span class="logo-mark"></span>
    <span class="logo-name">Harbor Crest</span>
  </div>
  <span class="abs nav current" style="left:429px">Home</span>
  <span class="abs nav" style="left:510px">About us</span>
  <span class="abs nav" style="left:623px">Services</span>
  <span class="abs nav" style="left:731px">Pricing</span>
  <span class="abs nav" style="left:829px">Contact</span>
  <a class="btn" style="left:938px;top:47px;width:150px;height:56px;font-size:15px">BOOK NOW</a>

  <h1 class="abs hero-title">Marine &amp;<br>Auto</h1>
  <ul class="abs checks">
    <li><svg width="18" height="18" viewBox="0 0 18 18"><circle cx="9" cy="9" r="9" fill="#fff"/><path d="M5 9.2l2.7 2.6L13 6.4" stroke="#1d3f7d" stroke-width="2" fill="none"/></svg>Shrink Wrapping</li>
    <li><svg width="18" height="18" viewBox="0 0 18 18"><circle cx="9" cy="9" r="9" fill="#fff"/><path d="M5 9.2l2.7 2.6L13 6.4" stroke="#1d3f7d" stroke-width="2" fill="none"/></svg>Mobile Detailing</li>
    <li><svg width="18" height="18" viewBox="0 0 18 18"><circle cx="9" cy="9" r="9" fill="#fff"/><path d="M5 9.2l2.7 2.6L13 6.4" stroke="#1d3f7d" stroke-width="2" fill="none"/></svg>Winterizing</li>
  </ul>
  <a class="btn" style="left:112px;top:492px;width:208px;height:62px;font-size:20px">GET A QUOTE</a>
  <div class="abs dots"><span class="on"></span><span></span><span></span></div>

  <!-- welcome -->
  <h2 class="abs welcome-title">Welcome to<br><span class="accent">Harbor Crest<br>Marine and Auto</span></h2>
  <p class="abs welcome-lead">We aim to run a company focused on providing customers in the lakes region of the central New Hampshire with a broad range of premium boats and cars services.</p>
  <p class="abs welcome-body">We are on a mission to support boat and car owners to keep their vessels and cars clean, well maintained, protected and safe wherever they are at convenient prices.</p>

  <!-- services -->
  <div class="abs services"></div>
  <h2 class="abs section-title" style="top:1072px">Our <span class="accent">Services</span></h2>

  <div class="abs card" style="left:112px">
    <div class="card-photo" role="img" aria-label="Row of boats on trailers shrink wrapped in blue for winter" style="background:linear-gradient(180deg,#dfe5ec 0%,#c8d3e0 45%,#2d52b8 70%,#6b6f78 100%)"></div>
    <h3>Shrink wrap for<br>boats</h3>
    <p>Nam libero tempore, cum soluta nobis est eligendi optio cumque nihil impedit quo minus id quo.</p>
    <a class="more">READ MORE</a>
  </div>
  <div class="abs card raised" style="left:445px">
    <div class="card-photo" role="img" aria-label="Polishing machine buffing a glossy vehicle panel" style="background:linear-gradient(135deg,#e9ebee 0%,#c6cacf 45%,#3a3e44 70%,#b3b7bc 100%)"></div>
    <h3>Mobile detailing for boats and cars</h3>
    <p>Nam libero tempore, cum soluta nobis est eligendi optio cumque nihil impedit quo minus id quo.</p>
    <a class="more">READ MORE</a>
  </div>
  <div class="abs card" style="left:778px">
    <div class="card-photo" role="img" aria-label="Boat fully covered in white shrink wrap in a snowy yard" style="background:linear-gradient(180deg,#cfdcea 0%,#eef2f6 50%,#dfe5ec 80%,#f4f6f8 100%)"></div>
    <h3>Mobile winterization for boats and much more</h3>
    <p>Nam libero tempore, cum soluta nobis est eligendi optio cumque nihil impedit quo minus id quo.</p>
    <a class="more">READ MORE</a>
  </div>

  <!-- pricing -->
  <h2 class="abs section-title" style="top:1784px">Our <span class="accent">Pricing</span></h2>
  <div class="abs price-circle" style="left:112px;top:1860px;width:452px;height:452px;border:1.5px solid var(--line)"></div>
  <div class="abs price-circle" style="left:636px;top:1860px;width:452px;height:452px;border:1.5px solid var(--line)"></div>
  <div class="abs price-circle" style="left:392px;top:1877px;width:416px;height:416px;background:linear-gradient(160deg,var(--orange-red) 0%,var(--orange) 100%)"></div>

  <div class="abs price-block" style="left:150px;top:1950px;width:250px">
    <h4>Boats</h4>
    <p><b>$19.00</b> per foot per boat for shrink wrapping</p>
    <p><b>$23.00</b> per foot for<br>boat detailing</p>
    <p><b>$200.00</b> for boat<br>winterization services</p>
  </div>
  <div class="abs price-hot" style="left:450px;top:1949px;width:300px">
    <h4>We will offer standard oil change and fluids plugs for boats starting at</h4>
    <p><b>$200.00</b> for 4 cylinder<br>inboards &amp; outboards</p>
    <p><b>$300.00</b> for 6 cylinder<br>inboards &amp; outboards</p>
    <p><b>$400.00</b> for 8 cylinder<br>inboards &amp; outboards</p>
  </div>
  <div class="abs price-block" style="left:815px;top:1950px;width:230px">
    <h4>Auto</h4>
    <p><b>$180.00</b> for standard<br>auto detailing</p>
    <p><b>$220.00</b> for premium<br>auto detailing</p>
  </div>

  <!-- what makes us different -->
  <div class="abs diff-photo" role="img" aria-label="Bow riders on trailers shrink wrapped in blue in a storage yard"></div>
  <div class="abs diff-panel"></div>
  <h2 class="abs diff-title">What makes us<br>different</h2>

  <div class="abs diff-item" style="top:2560px">
    <span class="diff-icon"><svg width="36" height="30" viewBox="0 0 36 30"><circle cx="18" cy="8" r="6" fill="#EE7325"/><circle cx="6" cy="11" r="4.5" fill="#EE7325"/><circle cx="30" cy="11" r="4.5" fill="#EE7325"/><path d="M8 30c0-8 4-14 10-14s10 6 10 14z" fill="#EE7325"/><path d="M0 26c0-6 2.5-10 6-10 2 0 3 1 4 2-2 3-3 6-3 8z" fill="#EE7325"/><path d="M36 26c0-6-2.5-10-6-10-2 0-3 1-4 2 2 3 3 6 3 8z" fill="#EE7325"/></svg></span>
    <span>First class<br>customer experience</span>
  </div>
  <div class="abs diff-item" style="top:2651px">
    <span class="diff-icon" style="color:var(--orange);font-size:36px;font-weight:500">$</span>
    <span>Capital intensive</span>
  </div>
  <div class="abs diff-item" style="top:2742px">
    <span class="diff-icon"><svg width="36" height="30" viewBox="0 0 36 30" fill="none" stroke="#EE7325" stroke-width="2.5"><path d="M2 2v26h32"/><path d="M7 22l8-9 6 5 10-11"/><path d="M25 7h6v6"/></svg></span>
    <span>Growing markets</span>
  </div>
  <div class="abs diff-item" style="top:2832px">
    <span class="diff-icon"><svg width="32" height="32" viewBox="0 0 32 32" fill="none" stroke="#EE7325" stroke-width="2.5"><path d="M14 6H5a2 2 0 00-2 2v19a2 2 0 002 2h19a2 2 0 002-2v-9"/><path d="M20 3h9v9"/><path d="M29 3L14 18"/></svg></span>
    <span>Negative externalities</span>
  </div>
  <div class="abs diff-item" style="top:2923px">
    <span class="diff-icon"><svg width="32" height="30" viewBox="0 0 32 30"><rect x="2" y="13" width="7" height="15" rx="1" fill="#EE7325"/><path d="M11 14l7-11c2-1 4 0 4 2l-2 7h8c2 0 3 2 3 3l-3 11c-.5 1.5-1.5 2-3 2H11z" fill="#EE7325"/></svg></span>
    <span>Convenient and competitive</span>
  </div>

  <!-- calendar booking -->
  <h2 class="abs section-title" style="top:3138px">Calendar <span class="accent">Booking</span></h2>

  <div class="abs calendar">
    <div class="cal-head">
      <svg width="12" height="16" viewBox="0 0 12 16"><path d="M9 2L3 8l6 6" stroke="#666" stroke-width="2" fill="none"/></svg>
      <span>SEPTEMBER 2021</span>
      <svg width="12" height="16" viewBox="0 0 12 16"><path d="M3 2l6 6-6 6" stroke="#666" stroke-width="2" fill="none"/></svg>
    </div>
    <div class="cal-grid">
      <div class="dow">MON</div><div class="dow">TUE</div><div class="dow">WED</div><div class="dow">THU</div><div class="dow">FRI</div><div class="dow">SAT</div><div class="dow">SUN</div>
      <div class="day">31</div><div class="day">1</div><div class="day booked">2</div><div class="day hold">3</div><div class="day">4</div><div class="day">5</div><div class="day">6</div>
      <div class="day booked">7</div><div class="day">8</div><div class="day booked">9</div><div class="day hold">10</div><div class="day">11</div><div class="day booked">12</div><div class="day booked">13</div>
      <div class="day booked">14</div><div class="day">15</div><div class="day">16</div><div class="day">17</div><div class="day">18</div><div class="day">19</div><div class="day">20</div>
      <div class="day">21</div><div class="day">22</div><div class="day">23</div><div class="day">24</div><div class="day hold">25</div><div class="day hold">26</div><div class="day hold">27</div>
      <div class="day booked">28</div><div class="day booked">29</div><div class="day">30</div><div class="day">1</div><div class="day">2</div><div class="day">3</div><div class="day">4</div>
    </div>
  </div>
  <div class="abs legend">
    <span><i style="background:var(--teal-pale)"></i>BOOKED</span>
    <span><i style="background:var(--orange-pale)"></i>ON HOLD</span>
    <span><i></i>AVAILABLE</span>
  </div>

  <div class="abs form-label" style="top:3222px">Client Information</div>
  <div class="field" style="left:624px;top:3269px;width:225px">Name</div>
  <div class="field" style="left:860px;top:3269px;width:228px">Email</div>
  <div class="field" style="left:624px;top:3323px;width:225px">Phone No</div>
  <div class="field" style="left:860px;top:3323px;width:228px">Address</div>

  <div class="abs form-label" style="top:3384px">Vehicle Information</div>
  <div class="toggle" style="left:784px;width:72px;background:var(--blue);color:var(--white)">BOAT</div>
  <div class="toggle" style="left:856px;width:71px;background:var(--blue-pale);color:var(--ink)">AUTO</div>

  <div class="field" style="left:624px;top:3481px;width:225px">Size</div>
  <div class="field" style="left:860px;top:3481px;width:228px">Year
    <svg width="10" height="16" viewBox="0 0 10 16"><path d="M1 6l4-4 4 4zM1 10l4 4 4-4z" fill="#555"/></svg>
  </div>
  <div class="field" style="left:624px;top:3535px;width:225px">Make</div>
  <div class="field" style="left:860px;top:3535px;width:228px">Model</div>
  <a class="btn" style="left:780px;top:3608px;width:150px;height:57px;font-size:15px">BOOK NOW</a>

  <!-- boats ready -->
  <div class="abs ready" role="img" aria-label="Friends cheering aboard a bow rider on the lake"></div>
  <svg class="abs" style="left:0;top:3743px" width="1200" height="601" viewBox="0 0 1200 601" aria-hidden="true">
    <path d="M0 420 C 80 560 250 612 460 590 C 760 560 1000 480 1200 470 L1200 601 L0 601 Z" fill="#fff"/>
  </svg>
  <h2 class="abs ready-title">Boats ready for<br>boating season</h2>
  <p class="abs ready-text">Nemo enim ipsam voluptatem quia voluptas sit aspernatur aut odit aut fugit, sed quia consuuntur gni dolores eos qui ratione voluptatem sequi nesciunt quia dolor sit amet, consectet.</p>
  <a class="btn" style="left:112px;top:4114px;width:206px;height:62px;font-size:20px">GET A QUOTE</a>

  <!-- footer -->
  <div class="abs" style="left:112px;top:4392px;display:flex;align-items:center;gap:12px">
    <span class="logo-mark" style="width:26px;height:26px"></span>
  </div>
  <div class="abs foot-name">Harbor Crest<br>Marine &amp; Auto</div>

  <div class="abs foot-head" style="left:514px">Quick Links</div>
  <ul class="abs foot-links">
    <li>Home</li><li>About us</li><li>Services</li><li>Pricing</li><li>Contact</li>
  </ul>

  <div class="abs foot-head" style="left:711px">Customer Support</div>
  <div class="abs foot-contact" style="top:4402px">
    <svg width="16" height="16" viewBox="0 0 16 16"><path d="M3 1l3 .5 1.2 3.3-1.8 1.4a9 9 0 004.4 4.4l1.4-1.8 3.3 1.2.5 3c0 .6-.5 1-1 1C7 14 2 9 2 2c0-.5.4-1 1-1z" fill="#EE7325"/></svg>
    1 555 010 0199
  </div>
  <div class="abs foot-contact" style="top:4457px">
    <svg width="18" height="14" viewBox="0 0 18 14"><rect x="0" y="0" width="18" height="14" rx="1.5" fill="#EE7325"/><path d="M1 1.5l8 6 8-6" stroke="#fff" stroke-width="1.5" fill="none"/></svg>
    info@harborcrestmarine.com
  </div>

  <div class="abs foot-rule"></div>
  <p class="abs copyright">© Harbor Crest Marine and Auto. All Rights Reserved. Privacy Policy | Terms &amp; Conditions.</p>
  <span class="abs social" style="left:948px"></span>
  <span class="abs social" style="left:997px"></span>
  <span class="abs social" style="left:1048px"></span>

</div>
</body>
</html>
```